Dental Design, very professional and noticable

Tindale Ridge Dental Surgery is based in Pelican Waters. We are a fast growing dental surgery and are looking for some professional business cards to send to patients.
We would like to see a design that is Vertical and uses the colours Soft Blue, Silver, White and Black. Maybe a full blue side with moto and details on back? Any other ideas or colours that you may think will make the card look unique is fine.
We need all details on the card that are listed above

Target Market(s)

Families, Retired, Other Professionals and Businesses

Industry/Entity Type

Dental

Contact Information for Business Card

Tindale Ridge Dental Surgery
Family, Cosmetic, Preventative
Dr. Owen Castrey
Dental Surgeon
BDS (Adel) FAE FADI FICD FPFA
phone: (07)50001846
fax: (07)50002917
email: tindaleridgedental@quillpost.com
http://tindaleridgedental.com/

Logo Text

Logo styles of interest
Abstract Logo
Requirements
Must have
• Vertical, Vibrant but Professional, Rounded Edges, Logo on front and back of card (different colours on each side)
Nice to have
• One side completely blue (not sure what shade) with logo and moto on bottom
Other side white, with blue or different coloured logo with details in black and silver?
Logo should show half circle with 1 end as arrow symbolizing pelican waters canal also a magnifine glass also half circled with 1 end as arrow. Any other ideas are welcome.
Should not have
• A tooth. A smile. Toothbrush or Toothpaste. Cornered edges.

```html
<!DOCTYPE html>
<html lang="en">
<head>
<meta charset="utf-8">
<title>Tindale Ridge Dental Surgery – Business Card</title>
<link href="https://fonts.googleapis.com/css2?family=Source+Sans+3:wght@400;600&display=swap" rel="stylesheet">
<style>
  :root {
    --page: #ffffff;
    --card-white: #ffffff;
    --card-blue: #6aa8fe;
    --card-edge: #a9b1b3;
    --silver-text: #8c9597;
    --brand-gold: #8a6c16;
    --motto-gold: #a8990f;
    --motto-gold-light: #bcae34;
  }
  * { margin: 0; padding: 0; box-sizing: border-box; }
  html, body { width: 1200px; height: 900px; overflow: hidden; background: var(--page); }
  body { position: relative; font-family: "Source Sans 3", sans-serif; }

  .card {
    position: absolute;
    top: 51px;
    width: 433px;
    height: 794px;
    border-radius: 24px;
    text-align: center;
  }
  .card--front { left: 153px; background: var(--card-white); border: 2px solid var(--card-edge); }
  .card--back  { left: 629px; background: var(--card-blue); border: 1px solid #9fc3f5; }

  .details { position: absolute; top: 66px; left: 0; right: 8px; color: var(--silver-text); }
  .details__name { font-size: 21px; font-weight: 600; letter-spacing: 0.3px; line-height: 26px; }
  .details__line { font-size: 17px; line-height: 23.5px; display: flex; justify-content: center; align-items: center; gap: 3px; }
  .details__line svg { width: 18px; height: 18px; flex: none; }
  .details__sep { margin: 0 3px; }

  .brand { position: absolute; left: 0; right: 0; }
  .brand__mark { display: block; margin: 0 auto; border-radius: 50%; background: var(--brand-gold); }
  .brand__name { color: var(--brand-gold); font-weight: 400; }
  .brand__motto { color: var(--motto-gold); }

  .card--front .brand { top: 646px; left: 0; right: 0; }
  .card--front .brand__mark { width: 56px; height: 56px; }
  .card--front .brand__name { font-size: 19px; margin-top: 14px; }
  .card--front .brand__motto { font-size: 14px; margin-top: 6px; }

  .card--back .brand { top: 570px; left: 0; right: 0; }
  .card--back .brand__mark { width: 74px; height: 74px; }
  .card--back .brand__name { font-size: 24px; margin-top: 14px; }
  .card--back .brand__motto { font-size: 17px; margin-top: 9px; color: var(--motto-gold-light); }
</style>
</head>
<body>
  <section class="card card--front" aria-label="Card front">
    <div class="details">
      <p class="details__name">DR. OWEN CASTREY</p>
      <p class="details__line">DENTAL SURGEON BDS</p>
      <p class="details__line">(Adel) FAE FADI FICD FPFA</p>
      <p class="details__line">
        <svg viewBox="0 0 18 18" aria-hidden="true"><path fill="#8c9597" d="M4 1.5 7 5 5.3 7a10 10 0 0 0 5.7 5.7L13 11l3.5 3-1.8 2.5C8 16 2 10 1.5 3.3Z"/></svg>
        (07)5000 1846<span class="details__sep">|</span>
        <svg viewBox="0 0 18 18" aria-hidden="true"><rect x="4" y="1" width="10" height="5" fill="#8c9597"/><rect x="1" y="6" width="16" height="8" rx="1.5" fill="#8c9597"/><rect x="4" y="11" width="10" height="6" fill="#fff" stroke="#8c9597" stroke-width="1.5"/></svg>
        (07)5000 2917
      </p>
      <p class="details__line">
        <svg viewBox="0 0 20 18" aria-hidden="true"><rect x="1.5" y="3" width="17" height="12" fill="none" stroke="#8c9597" stroke-width="1.5"/><path d="M1.5 3 10 10l8.5-7M1.5 15l6-6M18.5 15l-6-6" fill="none" stroke="#8c9597" stroke-width="1.3"/></svg>
        tindaleridgedental@quillpost.com
      </p>
      <p class="details__line">
        <svg viewBox="0 0 18 18" aria-hidden="true"><g fill="none" stroke="#b5bcbe" stroke-width="1"><circle cx="9" cy="9" r="7.5"/><ellipse cx="9" cy="9" rx="3.5" ry="7.5"/><path d="M1.5 9h15M3 5h12M3 13h12"/></g></svg>
        http://tindaleridgedental.com/
      </p>
    </div>
    <div class="brand">
      <span class="brand__mark" aria-hidden="true"></span>
      <p class="brand__name">Tindale Ridge Dental Surgery</p>
      <p class="brand__motto">Family, Cosmetic, Preventive</p>
    </div>
  </section>

  <section class="card card--back" aria-label="Card back">
    <div class="brand">
      <span class="brand__mark" aria-hidden="true"></span>
      <p class="brand__name">Tindale Ridge Dental Surgery</p>
      <p class="brand__motto">Family, Cosmetic, Preventive</p>
    </div>
  </section>
</body>
</html>
```